Business card design Needed for new logo / Construction business, home extensions and new builds

We need a business card design using our new logo files which i will attach to this project :)

We are a small construction business specialising in home extensions, new builds and property development. We are very ambitious and would appreciate professional and elegant designs for our new business card.

Very serious about using the services on BriefNest and recently acquired our new logo from here :)

Please get involved, i will feedback when i can as i am very busy but can respond daily, thanks

Target Market(s)

People that want to build onto their houses, new building developments or adding too their existing property

Industry/Entity Type

Construction

Contact Information for Business Card

Hollin Marsh Construction, Tobias Renwick (Managing Director), Tel 07822200444, email - info@hollin-marsh, www.hollin-marsh.co.uk

Colors

Designer to choose colors to be used in the design.

Requirements
Must have
• I like a deep grey on the back please. A lot of you have provided black from and back, try mixing things up a little. The black looks cool 😎 Thanks

```html
<!DOCTYPE html>
<html lang="en">
<head>
<meta charset="utf-8">
<title>Hollin Marsh Construction – Business Card</title>
<link rel="stylesheet" href="https://fonts.googleapis.com/css2?family=Cinzel:wght@500&family=Montserrat:wght@400;800&display=swap">
<style>
  :root {
    --page-bg: #d6d6d6;
    --card-white: #ffffff;
    --ink: #1b1b1b;
    --ink-soft: #3a3a3a;
    --card-grey: #36383b;
    --card-grey-deep: #2a2c2f;
    --gold: #d9a521;
    --sketch-light: #f4f4f4;
    --sketch-mid: #c4c4c4;
    --sketch-dark: #7d7d7d;
  }
  * { box-sizing: border-box; margin: 0; padding: 0; }
  html, body {
    width: 1200px; height: 846px; overflow: hidden;
    background: var(--page-bg);
  }
  .canvas {
    position: relative; width: 1200px; height: 846px;
    display: flex; align-items: center; justify-content: center; gap: 40px;
  }
  .card {
    position: relative; width: 520px; height: 336px; overflow: hidden;
    box-shadow: 0 10px 30px rgba(0,0,0,0.18);
  }

  /* Front */
  .card-front { background: var(--card-white); color: var(--ink); }
  .front-artwork {
    position: absolute; right: 0; top: 0; width: 290px; height: 250px;
    background:
      radial-gradient(ellipse at 62% 42%, var(--sketch-dark) 0%, var(--sketch-mid) 35%, var(--sketch-light) 68%, rgba(255,255,255,0) 100%);
    -webkit-mask-image: linear-gradient(to right, transparent 0%, #000 40%);
            mask-image: linear-gradient(to right, transparent 0%, #000 40%);
  }
  .front-brand {
    position: absolute; left: 34px; top: 52px;
    display: flex; align-items: center; gap: 10px;
  }
  .brand-square { width: 14px; height: 14px; background: var(--ink); flex: none; }
  .brand-name {
    font-family: "Cinzel", serif; font-weight: 500; font-size: 17px;
    letter-spacing: 0.5px; color: var(--ink); line-height: 1.2;
  }
  .front-person { position: absolute; left: 34px; top: 140px; }
  .person-name {
    font-family: "Montserrat", sans-serif; font-weight: 800; font-size: 21px;
    color: var(--ink);
  }
  .person-role {
    font-family: "Montserrat", sans-serif; font-weight: 400; font-size: 12px;
    color: var(--ink-soft); margin-top: 2px;
  }
  .contact-list {
    position: absolute; left: 34px; top: 212px; list-style: none;
    font-family: "Montserrat", sans-serif; font-weight: 400; font-size: 16px;
    color: var(--ink);
  }
  .contact-item { display: flex; align-items: center; gap: 10px; height: 28px; white-space: nowrap; }
  .contact-icon {
    width: 20px; height: 20px; background: var(--ink); flex: none;
    display: flex; align-items: center; justify-content: center;
  }
  .contact-icon svg { width: 14px; height: 14px; }

  /* Back */
  .card-back {
    background: linear-gradient(135deg, var(--card-grey) 0%, var(--card-grey-deep) 100%);
  }
  .back-texture {
    position: absolute; inset: 0;
    background: radial-gradient(ellipse at 40% 35%, rgba(255,255,255,0.06) 0%, rgba(255,255,255,0) 70%);
  }
  .back-brand {
    position: absolute; inset: 0;
    display: flex; align-items: center; justify-content: center; gap: 14px;
  }
  .back-brand .brand-square { width: 20px; height: 20px; background: var(--gold); }
  .back-brand .brand-name {
    color: var(--gold); font-size: 28px; text-align: center; letter-spacing: 1.5px;
  }
</style>
</head>
<body>
<main class="canvas">

  <section class="card card-front" aria-label="Business card front">
    <div class="front-artwork" role="img" aria-label="Pencil sketch of a two-storey house over faint architectural floor plans"></div>

    <div class="front-brand">
      <span class="brand-square"></span>
      <span class="brand-name">Hollin Marsh<br>Construction</span>
    </div>

    <div class="front-person">
      <p class="person-name">Tobias Renwick</p>
      <p class="person-role">Managing Director</p>
    </div>

    <ul class="contact-list">
      <li class="contact-item">
        <span class="contact-icon">
          <svg viewBox="0 0 24 24"><path fill="#fff" d="M6.6 10.8a15 15 0 0 0 6.6 6.6l2.2-2.2c.3-.3.7-.4 1-.2 1.1.4 2.3.6 3.6.6.6 0 1 .4 1 1V20c0 .6-.4 1-1 1A17 17 0 0 1 3 4c0-.6.4-1 1-1h3.5c.6 0 1 .4 1 1 0 1.3.2 2.5.6 3.6.1.3 0 .7-.2 1z"/></svg>
        </span>
        <span>07822 200 444</span>
      </li>
      <li class="contact-item">
        <span class="contact-icon">
          <svg viewBox="0 0 24 24"><rect x="3" y="6" width="18" height="12" fill="none" stroke="#fff" stroke-width="2"/><path d="M3 6l9 7 9-7" fill="none" stroke="#fff" stroke-width="2"/></svg>
        </span>
        <span>info@hollin-marsh.co.uk</span>
      </li>
      <li class="contact-item">
        <span class="contact-icon">
          <svg viewBox="0 0 24 24"><g fill="none" stroke="#fff" stroke-width="1.8"><circle cx="12" cy="12" r="9"/><ellipse cx="12" cy="12" rx="4" ry="9"/><path d="M3 12h18M5 7h14M5 17h14"/></g></svg>
        </span>
        <span>www.hollin-marsh.co.uk</span>
      </li>
    </ul>
  </section>

  <section class="card card-back" aria-label="Business card back">
    <div class="back-texture" role="img" aria-label="Faint embossed angular pattern on deep grey"></div>
    <div class="back-brand">
      <span class="brand-square"></span>
      <span class="brand-name">Hollin Marsh<br>Construction</span>
    </div>
  </section>

</main>
</body>
</html>
```